Kelvo Tech Oz Business card revamp

We are looking to revamp our business card design. We are hoping to change our colours to dark navey blue, gray, white and black but are open to keeping the same if a good design is submited. We are after somthing a bit differnt not just boring business card. I have attached a copy of our current card. We Want to keep the same logo design which i have attached a few to hopfully help you in this process. We are after a design that can be personalized to separate 4 people

Colors
0455a3
ffffff
000000
cbcbcb

Requirements
Must have
• Kelvo Tech Logo, address 3/41 Mallory Court, Wexhill 4218, phone number, Name and position

```html
<!DOCTYPE html>
<html lang="en">
<head>
<meta charset="utf-8">
<title>Kelvo Tech Oz – Business Card</title>
<link rel="stylesheet" href="https://fonts.googleapis.com/css2?family=Open+Sans:wght@400;600;700;800&display=swap">
<style>
  :root {
    --page-bg: #ecebe8;
    --card-white: #ffffff;
    --card-blue: #5b8fd0;
    --brand-blue: #2f6fc0;
    --brand-orange: #f07f2a;
    --ink: #2b2b2b;
    --divider: #3d78c6;
    --shadow: rgba(0, 0, 0, 0.18);
  }
  * { box-sizing: border-box; }
  html, body {
    margin: 0;
    width: 1200px;
    height: 738px;
    overflow: hidden;
    background: var(--page-bg);
    font-family: "Open Sans", Arial, sans-serif;
  }
  .stage {
    position: relative;
    width: 1200px;
    height: 738px;
  }
  .card {
    position: absolute;
    top: 219px;
    width: 520px;
    height: 300px;
    border-radius: 3px;
    box-shadow: 0 10px 28px var(--shadow);
  }
  .card--back {
    left: 60px;
    background: var(--card-blue);
    color: var(--card-white);
    text-align: center;
    padding-top: 62px;
  }
  .card--front {
    left: 620px;
    background: var(--card-white);
    color: var(--ink);
  }

  /* Brand name lockup */
  .brand {
    display: inline-flex;
    flex-direction: column;
    align-items: flex-start;
  }
  .brand__row {
    display: flex;
    align-items: center;
    gap: 10px;
  }
  .brand__dot {
    width: 30px;
    height: 30px;
    border-radius: 50%;
    background: var(--brand-orange);
  }
  .brand__name {
    font-weight: 800;
    font-size: 36px;
    line-height: 1;
    letter-spacing: -0.5px;
  }
  .brand__tagline {
    font-weight: 700;
    font-size: 15px;
    margin: 4px 0 0 40px;
  }
  .card--back .brand__name,
  .card--back .brand__tagline { color: var(--card-white); }
  .card--front .brand__name,
  .card--front .brand__tagline { color: var(--brand-blue); }

  /* Back: services */
  .services__title {
    margin: 26px 0 8px;
    font-size: 13px;
    font-weight: 700;
    letter-spacing: 0.5px;
    color: var(--brand-orange);
  }
  .services__text {
    margin: 0 auto;
    width: 430px;
    font-size: 12.5px;
    font-weight: 600;
    line-height: 1.45;
  }
  .services__bullet {
    display: inline-block;
    width: 7px;
    height: 7px;
    margin: 0 6px 1px;
    border-radius: 50%;
    background: var(--brand-orange);
  }

  /* Front: identity + contacts */
  .front__brand {
    position: absolute;
    left: 36px;
    top: 114px;
  }
  .front__divider {
    position: absolute;
    left: 322px;
    top: 52px;
    width: 2px;
    height: 176px;
    background: var(--divider);
  }
  .contact {
    position: absolute;
    left: 336px;
    top: 52px;
    margin: 0;
    padding: 0;
    list-style: none;
    font-size: 12.5px;
    font-weight: 600;
    line-height: 1.3;
  }
  .contact__item {
    display: flex;
    align-items: flex-start;
    gap: 8px;
    margin-bottom: 9px;
  }
  .contact__icon {
    flex: 0 0 13px;
    width: 13px;
    height: 13px;
    margin-top: 2px;
    fill: var(--divider);
  }
  .contact__name {
    font-size: 17px;
    font-weight: 600;
    color: var(--brand-blue);
    line-height: 1.1;
  }
  .contact__role {
    display: block;
    font-size: 12.5px;
    font-weight: 600;
    color: var(--brand-orange);
    margin-top: 2px;
  }
  .contact__item--person { margin-bottom: 12px; }
</style>
</head>
<body>
<main class="stage">

  <!-- Back of card -->
  <section class="card card--back" aria-label="Card back">
    <div class="brand">
      <div class="brand__row">
        <span class="brand__dot"></span>
        <span class="brand__name">Kelvo Tech</span>
      </div>
      <span class="brand__tagline">Passive Fire Protection</span>
    </div>
    <h2 class="services__title">OUR SERVICE</h2>
    <p class="services__text">
      This is Pixelcraft's version <span class="services__bullet"></span> of Lorem IpsumProin lorem velit auctor
      gravida nibh vel velit auctor aliquet <span class="services__bullet"></span> Aenean lorem quisauctor
      sollicitudin, lorem quis <span class="services__bullet"></span> bibendum auctor Lorem ipsum
    </p>
  </section>

  <!-- Front of card -->
  <section class="card card--front" aria-label="Card front">
    <div class="brand front__brand">
      <div class="brand__row">
        <span class="brand__dot"></span>
        <span class="brand__name">Kelvo Tech</span>
      </div>
      <span class="brand__tagline">Passive Fire Protection</span>
    </div>

    <div class="front__divider"></div>

    <ul class="contact">
      <li class="contact__item contact__item--person">
        <svg class="contact__icon" viewBox="0 0 16 16" aria-hidden="true"><circle cx="8" cy="4.5" r="3.5"/><path d="M1 16c0-4 3-6.5 7-6.5s7 2.5 7 6.5z"/></svg>
        <span><span class="contact__name">Dana Whitlow</span><span class="contact__role">Owner</span></span>
      </li>
      <li class="contact__item">
        <svg class="contact__icon" viewBox="0 0 16 16" aria-hidden="true"><path d="M8 0a5.5 5.5 0 0 0-5.5 5.5C2.5 10 8 16 8 16s5.5-6 5.5-10.5A5.5 5.5 0 0 0 8 0zm0 7.8a2.3 2.3 0 1 1 0-4.6 2.3 2.3 0 0 1 0 4.6z"/></svg>
        <span>3/41 Mallory Court<br>Wexhill 4218</span>
      </li>
      <li class="contact__item">
        <svg class="contact__icon" viewBox="0 0 16 16" aria-hidden="true"><path d="M3.6 0.8l2.3 2.9-1.4 2c.9 2 2.7 3.8 4.8 4.8l2-1.4 2.9 2.3-1.4 2.9C7 14.9 1.1 9 0.8 3.6z"/></svg>
        <span>361 555 0148</span>
      </li>
      <li class="contact__item">
        <svg class="contact__icon" viewBox="0 0 16 16" aria-hidden="true"><path d="M1 3h14v1.2L8 9 1 4.2z"/><path d="M1 5.8l7 4.8 7-4.8V13H1z"/></svg>
        <span>dana@kelvotech.com.au</span>
      </li>
      <li class="contact__item">
        <svg class="contact__icon" viewBox="0 0 16 16" aria-hidden="true"><circle cx="8" cy="8" r="7"/><path d="M1 8h14M8 1c2.5 2.5 2.5 11.5 0 14M8 1c-2.5 2.5-2.5 11.5 0 14" stroke="#fff" stroke-width="1" fill="none"/></svg>
        <span>www.kelvotech.com.au</span>
      </li>
    </ul>
  </section>

</main>
</body>
</html>
```